Brand new redesign of Brightwell finance website

I need a new website design that i can advertise a great low interest rate on the front page and capture input application details that will send through to my email address.

some car finance companies will be similar to this would be listed below

quorvaloans.com.au
pelmarfinance.com.au
finance715.com.au
gundrelfinance.com.au
finance93.com.au
Updates

Project Deadline Extended
Reason: I have changed the project to a committed project. all the webpages should have the same format just different content and i want to be able to edit the front page easily to update my interest rates.

Project Deadline Extended
Reason: Provide more time for resubmission and submission work

Target Market(s)

Australian Finance market targeting a younger demographic

Industry/Entity Type

Finance

Coding

Coded - Design and coding required

Number of Pages Required

5+ page

Font styles to use
Serif
Sans Serif

Colors
0255a3
ffffff
cedeed

Requirements
Must have
• application capture form
• apply now buttons
• Headline rate front page

```html
<!DOCTYPE html>
<html lang="en">
<head>
<meta charset="utf-8">
<title>Brightwell Finance</title>
<link href="https://fonts.googleapis.com/css2?family=Lato:wght@400;700&family=Roboto+Condensed:wght@400;700&display=swap" rel="stylesheet">
<style>
:root{
  --brand:#0255a3;
  --brand-mid:#1f5fb8;
  --brand-soft:#cedeed;
  --ink:#231f20;
  --ink-deep:#0d0d0d;
  --text:#555;
  --white:#ffffff;
  --panel:#3b4658;
}
*{margin:0;padding:0;box-sizing:border-box}
html,body{width:815px;height:1200px;overflow:hidden}
body{position:relative;font-family:'Lato',sans-serif;background:var(--white);color:var(--ink)}
.cond{font-family:'Roboto Condensed',sans-serif}
.abs{position:absolute}

.topbar{left:0;top:0;width:815px;height:29px;background:var(--ink);color:var(--white)}
.topbar .call{position:absolute;right:184px;top:8px;font-size:10px;font-family:'Roboto Condensed',sans-serif}
.topbar .call b{font-weight:400;font-size:11px;margin-left:3px}
.social{position:absolute;top:5px;display:flex;gap:4px}
.social span{width:19px;height:19px;border-radius:50%;background:var(--ink-deep);border:1px solid #444}

.header{left:0;top:29px;width:815px;height:70px;background:var(--white)}
.logo{position:absolute;left:87px;top:8px;width:90px;text-align:center}
.logo .mark{width:48px;height:48px;border-radius:50%;background:#8a8a8a;margin:0 auto 4px}
.logo .name{font-size:11px;font-weight:700;color:#777;letter-spacing:1px;line-height:1.1}
.nav{position:absolute;left:212px;top:23px;display:flex;align-items:center;gap:0;font-family:'Roboto Condensed',sans-serif;font-size:11px}
.nav a{color:var(--ink);text-decoration:none;padding:5px 10px}
.nav .active{background:var(--brand-mid);color:var(--white);border-radius:13px;padding:6px 13px}
.nav .apply{background:var(--ink-deep);color:var(--white);font-weight:700;margin-left:3px;padding:6px 8px}

.hero{left:0;top:99px;width:815px;height:291px;background:linear-gradient(90deg,#27508f 0%,#5e7fb4 40%,#8fa8cc 70%,#6e8cbc 100%)}
.hero-copy{position:absolute;left:109px;top:68px;color:var(--white)}
.hero-copy h1{font-size:23px;font-weight:700;line-height:28px}
.rate{margin-left:6px;margin-top:16px}
.rate h2{font-size:18px;font-weight:700}
.rate p{font-size:12px;font-weight:700;width:162px;border-bottom:1px solid rgba(255,255,255,.7);padding:6px 0 5px}
.btn-dark{display:inline-block;background:var(--ink-deep);color:var(--white);font-size:10px;font-weight:700;padding:5px 11px;border-radius:2px;margin:19px 0 0 5px}

.quote{position:absolute;left:523px;top:35px;width:205px;height:230px;background:var(--panel);border-radius:2px;overflow:hidden}
.quote svg{position:absolute;left:0;top:0}
.quote h3{position:absolute;top:10px;width:100%;text-align:center;font-family:'Roboto Condensed',sans-serif;color:var(--brand);font-size:17px;font-weight:700}
.quote .fields{position:absolute;left:12px;top:56px;width:181px}
.quote .field{height:22px;background:var(--white);border-radius:2px;font-size:7.5px;color:#777;padding:6px 7px;margin-bottom:12px}
.quote .submit{height:25px;background:var(--brand);color:var(--white);font-size:11px;font-weight:700;text-align:center;line-height:25px;border-radius:2px}

.about{left:0;top:390px;width:815px;height:211px;background:linear-gradient(#f6f6f6,#fff);text-align:center}
.about h2{margin-top:26px;font-size:21px;font-weight:700}
.dot{width:16px;height:14px;border-radius:50%;margin:14px auto 0}
.about p{width:630px;margin:13px auto 0;font-size:8.6px;line-height:15px;color:var(--text)}
.btn-blue{display:inline-block;background:var(--brand);color:var(--white);font-size:9px;font-weight:700;padding:5px 9px;border-radius:2px;margin-top:13px}

.services{left:0;top:601px;width:815px;height:242px;background:var(--brand-mid);text-align:center}
.services h2{margin-top:24px;font-size:21px;font-weight:700;color:var(--white)}
.card{position:absolute;top:86px;width:149px;height:125px}
.card .photo{height:96px}
.card .cap{height:29px;background:var(--ink-deep);color:var(--white);font-family:'Roboto Condensed',sans-serif;font-size:11px;text-align:left;padding:9px 0 0 56px}
.card .badge{position:absolute;left:14px;top:94px;width:37px;height:37px;border-radius:50%;background:var(--white);border:3px solid var(--ink-deep)}

.repay{left:87px;top:873px;width:641px;height:81px;background:linear-gradient(90deg,#3a3a3a,#2c3540 60%,#2d3742)}
.repay h2{position:absolute;left:33px;top:20px;font-family:'Roboto Condensed',sans-serif;font-size:20px;font-weight:700;color:var(--white)}
.repay p{position:absolute;left:34px;top:50px;font-family:'Roboto Condensed',sans-serif;font-size:11px;color:var(--white)}
.repay .btn-blue{position:absolute;right:16px;top:28px;margin:0;font-size:9px;padding:6px 8px}

.newsletter{left:0;top:984px;width:815px;height:132px;background:var(--ink)}
.newsletter h2{position:absolute;left:176px;top:34px;color:var(--white);font-size:21px;font-weight:700}
.newsletter .input{position:absolute;left:179px;top:70px;width:238px;height:26px;background:var(--white);font-size:8px;padding:8px 7px;color:#333}
.newsletter .go{position:absolute;left:423px;top:70px;width:58px;height:26px;background:var(--brand-mid);color:var(--white);font-family:'Roboto Condensed',sans-serif;font-weight:700;font-size:13px;text-align:center;line-height:26px}

.footnav{left:0;top:1116px;width:815px;height:34px;background:var(--ink-deep);display:flex;justify-content:center;align-items:center;gap:12px;font-family:'Roboto Condensed',sans-serif;font-size:10px;color:var(--white)}
.footnav i{font-style:normal;color:#999;font-size:7px}

.copy{left:0;top:1150px;width:815px;height:50px;background:var(--brand-mid);color:var(--white)}
.copy p{position:absolute;left:87px;top:20px;font-size:7.5px;font-weight:700}
.copy .follow{position:absolute;left:592px;top:21px;font-size:8px;font-weight:700}
.copy .social span{background:var(--ink-deep);border:2px solid var(--white);width:20px;height:20px}
</style>
</head>
<body>

<div class="abs topbar">
  <div class="call">Worried About Finance? <b>Call 1300 555 418</b></div>
  <div class="social" style="left:636px"><span></span><span></span><span></span><span></span></div>
</div>

<header class="abs header">
  <div class="logo"><div class="mark"></div><div class="name">BRIGHTWELL FINANCE</div></div>
  <nav class="nav">
    <a class="active">Home</a><a>About Us</a><a>Services</a><a>Terms Of Use</a><a>Privacy Policy</a><a>Loan Calculator</a><a>Contact us</a><a class="apply">Apply Now</a>
  </nav>
</header>

<section class="abs hero" role="img" aria-label="Blurred photo of a car key being handed over">
  <div class="hero-copy">
    <h1>We Providing Lowest<br>Interest Rate</h1>
    <div class="rate">
      <h2>Rate :</h2>
      <p>4.69%</p>
      <p>4.99%</p>
    </div>
    <span class="btn-dark">Compare</span>
  </div>
  <form class="quote">
    <svg width="205" height="42" viewBox="0 0 205 42"><polygon points="0,0 205,0 205,30 102,41 0,30" fill="#fff"/></svg>
    <h3>Quick Quote</h3>
    <div class="fields">
      <div class="field">Name *</div>
      <div class="field">Telephone *</div>
      <div class="field">Email *</div>
      <div class="field">Employment Status *</div>
      <div class="submit">APPLY NOW</div>
    </div>
  </form>
</section>

<section class="abs about">
  <h2>About Brightwell Finance</h2>
  <div class="dot" style="background:#9a9a9a"></div>
  <p>Lorem Ipsum is simply dummy text of the printing and typesetting industry. Lorem Ipsum has been the industry's standard dummy text ever since the 1500s, when an unknown printer took a galley of type and scrambled it to make a type specimen book. It has survived not only five centuries, but also the leap into electronic typesetting, remaining essentially unchanged. It was popularised in the 1960s with the release of Letraset sheets containing Lorem Ipsum passages, and more recently with desktop publishing software</p>
  <span class="btn-blue">Read more</span>
</section>

<section class="abs services">
  <h2>Our Services</h2>
  <div class="dot" style="background:#0f3c7a"></div>
  <div class="card" style="left:87px"><div class="photo" role="img" aria-label="Photo of car keys handed across a desk" style="background:linear-gradient(135deg,#e9e2da,#b9a89a)"></div><div class="cap">Vehicle Loans</div><div class="badge"></div></div>
  <div class="card" style="left:252px"><div class="photo" role="img" aria-label="Photo of a speedboat on the water" style="background:linear-gradient(#dfe7ee,#8fa3b6)"></div><div class="cap">Boat Loans</div><div class="badge"></div></div>
  <div class="card" style="left:416px"><div class="photo" role="img" aria-label="Photo of a model house held in hands" style="background:linear-gradient(#3f9ad8,#c98a4e)"></div><div class="cap">Home Loans</div><div class="badge"></div></div>
  <div class="card" style="left:580px"><div class="photo" role="img" aria-label="Photo of fingers walking up stacks of coins" style="background:linear-gradient(135deg,#f2f2f2,#a8a39c)"></div><div class="cap">Personal Loans</div><div class="badge"></div></div>
</section>

<section class="abs repay">
  <h2>What will my repayments be?</h2>
  <p>See how much you could borrow with our loan calculator.</p>
  <span class="btn-blue">Loan Calculator</span>
</section>

<section class="abs newsletter">
  <div class="abs" role="img" aria-label="Cartoon businessman waving" style="left:76px;top:14px;width:72px;height:112px;background:#3a3a3a;border-radius:30px 30px 6px 6px"></div>
  <h2>Newsletter Signup</h2>
  <div class="input">Enter your email</div>
  <div class="go">Go</div>
  <div class="abs" role="img" aria-label="Illustration of a blue classic sports car" style="left:556px;top:16px;width:222px;height:108px;background:radial-gradient(ellipse at 55% 45%,#2a43d8 0%,#1a2a8a 45%,rgba(35,31,32,0) 72%)"></div>
</section>

<nav class="abs footnav">
  <span>Home</span><i>::</i><span>About Us</span><i>::</i><span>Services</span><i>::</i><span>Terms Of Use</span><i>::</i><span>Privacy Policy</span><i>::</i><span>Loan Calculator</span><i>::</i><span>Contact us</span>
</nav>

<footer class="abs copy">
  <p>Copyright © 2016 Brightwellfinance &nbsp;| All rights reserved.</p>
  <span class="follow">Follow Us</span>
  <div class="social" style="left:637px;top:15px"><span></span><span></span><span></span><span></span></div>
</footer>

</body>
</html>
```